Law Office Business Card

We need a business card design to include the following information:
Name of Firm: Brennick Law Group, P.A.
Address: 4627 Sandlot Ave, Ste 208, Lakemont Shores, FL 34999
Phone: 561-555-0148
Fax: 561-555-0193
Website: http://www.tbrennicklaw.example

We Need a place for the Person's name and email address. Please start with the following:
Lorna K. Dwyer, Esq.
lorna@tbrennicklaw.example

```html
<!DOCTYPE html>
<html lang="en">
<head>
<meta charset="utf-8">
<title>Brennick Law Group – Business Card</title>
<link rel="stylesheet" href="https://fonts.googleapis.com/css2?family=Crimson+Pro:wght@400;600&display=swap">
<style>
  :root {
    --page-bg: #e8e6e2;
    --card-bg: #ffffff;
    --ink: #2f2f31;
    --band-dark: #2a2a2c;
    --band-blue: #1b5278;
    --name-blue: #1f5a82;
    --brand-taupe: #8a7e70;
    --band-text: #ffffff;
  }
  * { margin: 0; padding: 0; box-sizing: border-box; }
  html, body {
    width: 1200px; height: 1200px; overflow: hidden;
    background: var(--page-bg);
    font-family: "Crimson Pro", Georgia, serif;
    color: var(--ink);
  }
  .canvas {
    position: relative; width: 1200px; height: 1200px;
    display: flex; flex-direction: column; align-items: center; justify-content: center;
    gap: 60px;
  }
  .card {
    position: relative; width: 900px; height: 511px;
    background: var(--card-bg);
    box-shadow: 0 6px 20px rgba(0,0,0,0.14);
    overflow: hidden;
  }
  /* front */
  .corner-accent-blue { position: absolute; left: 0; top: 0; width: 121px; height: 59px; background: var(--band-blue); }
  .corner-accent-dark { position: absolute; left: 0; top: 0; width: 109px; height: 95px; background: var(--band-dark); }

  .brand-mark {
    position: absolute; display: flex; flex-direction: column; align-items: center; gap: 12px;
    color: var(--brand-taupe); font-weight: 400; letter-spacing: 0.04em;
    text-transform: uppercase; line-height: 1.1; text-align: center;
  }
  .brand-mark .brand-square { flex: none; border: 2px solid var(--brand-taupe); }
  .front .brand-mark { left: 120px; top: 110px; width: 260px; font-size: 30px; }
  .front .brand-square { width: 56px; height: 56px; }

  .person { position: absolute; left: 510px; top: 46px; }
  .person-name { color: var(--name-blue); font-size: 36px; font-weight: 600; line-height: 1; white-space: nowrap; }
  .person-name .surname { font-size: 27px; font-weight: 600; }
  .person-email { margin-top: 8px; font-size: 26px; color: var(--ink); }

  .firm-name {
    position: absolute; left: 47px; top: 322px;
    font-size: 32px; font-weight: 400; letter-spacing: 0.01em; text-transform: uppercase; line-height: 1;
  }
  .rule-blue { position: absolute; left: 0; right: 0; top: 362px; height: 7px; background: var(--band-blue); }
  .band-address {
    position: absolute; left: 0; right: 0; top: 374px; height: 56px;
    background: var(--band-dark); color: var(--band-text);
    display: flex; align-items: center; gap: 4px; padding-left: 46px; font-size: 26px;
  }
  .band-contact {
    position: absolute; left: 0; right: 0; top: 430px; height: 66px;
    background: var(--band-blue); color: var(--band-text);
    font-size: 26px;
  }
  .band-foot { position: absolute; left: 0; right: 0; top: 496px; bottom: 0; background: var(--band-dark); }
  .contact-item { position: absolute; top: 50%; transform: translateY(-50%); display: flex; align-items: center; gap: 6px; white-space: nowrap; }
  .contact-phone { left: 44px; }
  .contact-fax { left: 287px; }
  .contact-web { left: 540px; }
  .icon { width: 18px; height: 18px; flex: none; fill: var(--band-text); }

  /* back */
  .back .brand-mark { left: 50%; top: 50%; transform: translate(-50%, -50%); font-size: 34px; }
  .back .brand-square { width: 64px; height: 64px; }
</style>
</head>
<body>
<main class="canvas">

  <section class="card front" aria-label="Business card front">
    <div class="corner-accent-blue"></div>
    <div class="corner-accent-dark"></div>

    <div class="brand-mark">
      <span class="brand-square"></span>
      <span>Brennick Law<br>Group</span>
    </div>

    <div class="person">
      <p class="person-name">LORNA K. <span class="surname">Dwyer, Esq.</span></p>
      <p class="person-email">lorna@tbrennicklaw.example</p>
    </div>

    <h1 class="firm-name">Brennick Law Group, P.A.</h1>

    <div class="rule-blue"></div>
    <div class="band-address">
      <svg class="icon" viewBox="0 0 24 24" aria-hidden="true"><path d="M12 1C7.6 1 4 4.5 4 8.9 4 14.8 12 23 12 23s8-8.2 8-14.1C20 4.5 16.4 1 12 1zm0 11a3 3 0 1 1 0-6 3 3 0 0 1 0 6z"/></svg>
      <span>4627 Sandlot Ave, Ste 208, Lakemont Shores, FL 34999</span>
    </div>
    <div class="band-contact">
      <span class="contact-item contact-phone">
        <svg class="icon" viewBox="0 0 24 24" aria-hidden="true"><path d="M6.6 10.8a15.1 15.1 0 0 0 6.6 6.6l2.2-2.2c.3-.3.7-.4 1-.2 1.1.4 2.3.6 3.6.6.6 0 1 .4 1 1V20c0 .6-.4 1-1 1C10.6 21 3 13.4 3 4c0-.6.4-1 1-1h3.5c.6 0 1 .4 1 1 0 1.3.2 2.5.6 3.6.1.3 0 .7-.2 1z"/></svg>
        561-555-0148
      </span>
      <span class="contact-item contact-fax">
        <svg class="icon" viewBox="0 0 24 24" aria-hidden="true"><path d="M6 2h9l3 3v4H6z M3 10h18v9h-3v3H6v-3H3z M8 16v4h8v-4z"/></svg>
        561-555-0193
      </span>
      <span class="contact-item contact-web">
        <svg class="icon" viewBox="0 0 24 24" aria-hidden="true"><path d="M12 2a10 10 0 1 0 0 20 10 10 0 0 0 0-20zm0 2c.9 0 2.2 1.8 2.8 5H9.2C9.8 5.8 11.1 4 12 4zM4.3 11h4.6c0 .7 0 1.4.1 2H4.3a8 8 0 0 1 0-2zm.8 4h4.2c.3 1.6.8 3 1.4 4a8 8 0 0 1-5.6-4zm4-6H5.1a8 8 0 0 1 5.6-4c-.6 1-1.1 2.4-1.4 4zm2.9 11c-.9 0-2.2-1.8-2.8-5h5.6c-.6 3.2-1.900 5-2.8 5zm3-7h-6c-.1-.6-.1-1.3-.1-2h6.2c0 .7 0 1.4-.1 2zm.3 6c.6-1 1.1-2.4 1.4-4h4.2a8 8 0 0 1-5.6 4zm1.7-6c.1-.6.1-1.3.1-2h4.6a8 8 0 0 1 0 2zm-.3-4c-.3-1.6-.8-3-1.4-4a8 8 0 0 1 5.6 4z"/></svg>
        www.tbrennicklaw.example
      </span>
    </div>
    <div class="band-foot"></div>
  </section>

  <section class="card back" aria-label="Business card back">
    <div class="brand-mark">
      <span class="brand-square"></span>
      <span>Brennick Law<br>Group</span>
    </div>
  </section>

</main>
</body>
</html>
```